Velnimo.org
Brackwater Residents association
plz star rating....
in the back of the card it should have the following
K&T BULKWARE SUPPLIERS
847 HAZELMOOR ROAD
OLVERTON MA. 02946
we will like the back ground of the card to be red... our colors are red yellow and blue.

```html
<!DOCTYPE html>
<html lang="en">
<head>
<meta charset="utf-8">
<title>Velnimo.org Stationery</title>
<link href="https://fonts.googleapis.com/css2?family=Open+Sans:wght@400;600;700&display=swap" rel="stylesheet">
<style>
:root{
  --stage:#e9e4dc;
  --paper:#ffffff;
  --blue:#1c9ad8;
  --blue-light:#7cc6ea;
  --yellow:#e6b41e;
  --red:#d2232a;
  --ink:#5a5a5a;
  --label:#4a4038;
  --grey:#6e6e6e;
  --shadow:0 1px 4px rgba(0,0,0,.25);
}
*{margin:0;padding:0;box-sizing:border-box}
html,body{width:1200px;height:446px;overflow:hidden}
body{background:var(--stage);font-family:"Open Sans",sans-serif;color:var(--ink);position:relative}
.piece{position:absolute;background:var(--paper);box-shadow:var(--shadow);overflow:hidden}
.label{position:absolute;font-size:6px;letter-spacing:1px;text-transform:uppercase;color:var(--label);white-space:nowrap}
.brand{color:var(--yellow);font-weight:700;white-space:nowrap;display:flex;align-items:center;gap:3px;line-height:1}
.brand-dot{display:inline-block;background:var(--blue);border-radius:50%;flex:none}
.faint{opacity:.14}

/* business cards */
.card{left:19px;width:78px;height:39px}
.card-front{top:173px}
.card-front .panel{position:absolute;right:0;top:0;width:38px;height:100%;background:var(--blue)}
.card-front .brand{position:absolute;left:4px;top:15px;font-size:5px}
.card-front .panel p{font-size:2.6px;color:#fff;margin:11px 0 0 4px;line-height:4px}
.card-back{top:236px;background:var(--red)}
.card-back p{font-size:3px;color:#fff;text-align:center;margin-top:13px;line-height:4.5px;font-weight:600}

/* letterheads */
.letterhead{top:12px;width:224px;height:396px}
.lh-one{left:163px}
.lh-two{left:413px}
.lh-one .brand{position:absolute;left:16px;top:14px;font-size:10px}
.lh-one .contact{position:absolute;right:16px;top:14px;font-size:3.2px;line-height:4.6px;text-align:right}
.watermark{position:absolute;left:0;right:0;display:flex;justify-content:center}
.watermark .brand{font-size:26px;gap:6px}
.lh-one .watermark{top:170px}
.lh-two .watermark{top:178px}
.lh-two .footer-text{position:absolute;bottom:34px;left:0;right:0;text-align:center;font-size:3.2px;white-space:nowrap}
.band{position:absolute;left:0;right:0;bottom:12px;height:10px}
.band i{display:block;height:2px;margin-top:2px;background:var(--blue)}
.band i:first-child{background:var(--blue-light)}

/* envelopes */
.envelope{width:352px}
.env-back{left:842px;top:0;height:96px}
.env-back .strip{height:34px;background:var(--blue)}
.env-flap{left:818px;top:96px;height:86px}
.env-open{left:842px;top:150px;height:92px}
.env-open .brand{position:absolute;left:118px;top:44px;font-size:9px}
.env-front{left:797px;top:312px;width:398px;height:100px}
.env-front .brand{position:absolute;left:18px;top:14px;font-size:9px}
.env-front .sub{position:absolute;left:18px;top:28px;font-size:3px;white-space:nowrap}
.env-front .band{bottom:8px}
svg{display:block}
</style>
</head>
<body>
  <div class="label" style="left:19px;top:72px">Stationery Designs</div>

  <div class="piece card card-front">
    <div class="brand"><span class="brand-dot" style="width:3px;height:3px"></span>Velnimo.org</div>
    <div class="panel"><p>Brackwater Residents<br>association<br>555-0142</p></div>
  </div>
  <div class="label" style="left:19px;top:218px;font-size:4px">Business Card Front</div>

  <div class="piece card card-back">
    <p>K&amp;T BULKWARE SUPPLIERS<br>847 HAZELMOOR ROAD<br>OLVERTON MA. 02946</p>
  </div>
  <div class="label" style="left:19px;top:282px;font-size:4px">Business Card Back</div>

  <div class="piece letterhead lh-one">
    <div class="brand"><span class="brand-dot" style="width:6px;height:6px"></span>Velnimo.org</div>
    <div class="contact">847 Hazelmoor Road<br>Olverton MA. 02946<br>555-0142<br>info@velnimo.org</div>
    <div class="watermark faint"><div class="brand"><span class="brand-dot" style="width:14px;height:14px"></span>Velnimo.org</div></div>
    <div class="band"><i></i><i></i></div>
  </div>
  <div class="label" style="left:240px;top:427px">Letterhead Option 1</div>

  <div class="piece letterhead lh-two">
    <div class="watermark faint"><div class="brand"><span class="brand-dot" style="width:14px;height:14px"></span>Velnimo.org</div></div>
    <div class="footer-text">847 Hazelmoor Road, Olverton MA. 02946 · 555-0142 · info@velnimo.org</div>
    <div class="band"><i></i><i></i></div>
  </div>
  <div class="label" style="left:490px;top:427px">Letterhead Option 2</div>

  <div class="piece envelope env-back"><div class="strip"></div></div>

  <div class="piece envelope env-flap">
    <svg width="352" height="86" viewBox="0 0 352 86">
      <path d="M0 0 H352 V22 L192 72 Q176 77 160 72 L0 22 Z" fill="var(--grey)"/>
    </svg>
  </div>

  <div class="piece envelope env-open">
    <svg width="352" height="92" viewBox="0 0 352 92" style="position:absolute;top:0;left:0">
      <path d="M0 0 L176 38 L352 0" fill="none" stroke="#ddd" stroke-width="1"/>
    </svg>
    <div class="brand"><span class="brand-dot" style="width:6px;height:6px"></span>Velnimo.org</div>
  </div>

  <div class="piece envelope env-front">
    <div class="brand"><span class="brand-dot" style="width:6px;height:6px"></span>Velnimo.org</div>
    <div class="sub">847 Hazelmoor Road, Olverton MA. 02946</div>
    <div class="band"><i></i><i></i></div>
  </div>
  <div class="label" style="left:862px;top:427px">Envelope Design</div>
</body>
</html>
```